Corvane Ridge PowerPoint Design

Take info off of the website and come up with a PowerPoint Template

www.corvaneridge.com

Target Market(s)

Size Reduction Equipment

Colors
3176b5

Requirements
Must have
• a nice template
Nice to have
• Innovative but good for wood products industry

```html
<!DOCTYPE html>
<html lang="en">
<head>
<meta charset="UTF-8">
<title>Corvane Ridge — PowerPoint Design</title>
<link href="https://fonts.googleapis.com/css2?family=Lato:wght@300;400;700&family=Raleway:wght@200;300&display=swap" rel="stylesheet">
<style>
  :root{
    --brand-blue:#3176b5;
    --band-blue:#2f6cb5;
    --title-blue:#2c6db5;
    --yellow:#f7c100;
    --orange:#ef7d22;
    --grey-text:#8a8a8a;
    --dark-text:#333;
    --frame:#d4d4d4;
    --rule-grey:#8c8c8c;
  }
  *{box-sizing:border-box;margin:0;padding:0}
  html,body{width:1200px;height:1200px;overflow:hidden;background:#fff}
  body{position:relative;font-family:"Lato",Arial,sans-serif}

  .side-band{position:absolute;left:0;top:0;width:117px;height:1170px;background:var(--band-blue)}
  .side-title{position:absolute;left:0;width:117px;text-align:center;color:#fff;
    font-family:"Raleway",Arial,sans-serif;font-weight:200;font-size:50px;line-height:56px}
  .side-title span{display:block}
  .side-title.word-one{top:110px}
  .side-title.word-two{top:716px}

  .base-rule{position:absolute;left:0;top:1172px;width:1052px;height:6px;background:var(--rule-grey)}
  .base-brand{position:absolute;left:1054px;top:1140px;font-weight:700;font-size:34px;color:#6f6f6f;letter-spacing:-1px}

  .slide{position:absolute;width:458px;height:257px;background:#fff;border:1px solid var(--frame);overflow:hidden}
  .col-a{left:169px}.col-b{left:686px}
  .row-1{top:30px}.row-2{top:308px}.row-3{top:586px}.row-4{top:865px}

  .abs{position:absolute}
  .accent{position:absolute;left:21px;top:14px;width:18px;height:32px;background:var(--yellow)}
  .accent::after{content:"";position:absolute;left:10px;top:8px;width:24px;height:1px;background:var(--title-blue)}
  .slide-title{position:absolute;left:45px;top:27px;font-size:12px;color:var(--title-blue);font-weight:400}
  .footer-rule{position:absolute;left:26px;top:242px;width:384px;height:2px;background:var(--brand-blue)}
  .footer-brand{position:absolute;left:412px;top:236px;font-size:8px;font-weight:700;color:#666}

  .body-copy{font-size:4.6px;line-height:7.6px;color:var(--grey-text)}
  .body-copy p+p{margin-top:7px}

  /* cover */
  .cover{background:#000;border-color:#bbb}
  .cover-photo{left:99px;top:62px;width:264px;height:64px}
  .cover-title{left:0;width:458px;top:132px;text-align:center;color:#eee;font-size:13.5px;font-weight:300}
  .cover-sub{left:0;width:458px;top:148px;text-align:center;color:#bbb;font-size:5px;letter-spacing:1.2px}
  .cover-brand{left:0;width:458px;top:218px;text-align:center;color:#fff;font-size:14px;font-weight:700}

  /* about */
  .about-photo{left:0;top:0}
  .about-lead{right:336px;top:152px;text-align:right;color:var(--title-blue);font-size:8.6px;line-height:11.4px}
  .about-body{left:136px;top:156px;width:282px;font-size:4.7px;line-height:9px}

  /* true blue */
  .heritage-accent{left:281px;top:34px;width:23px;height:42px;background:var(--yellow)}
  .heritage-title{right:164px;top:49px;text-align:right;color:var(--title-blue);font-size:10.5px;line-height:14px}
  .heritage-photo{left:0;top:110px;width:294px;height:89px}
  .heritage-body{left:304px;top:108px;width:130px;font-size:4.2px;line-height:7.2px}

  /* two column */
  .two-col-left{left:45px;top:76px;width:148px}
  .two-col-right{left:265px;top:76px;width:148px}
  .two-col-divider{left:230px;top:73px;width:0;height:133px;border-left:1px dashed #bbb}

  /* three column */
  .three-col{top:98px;width:94px;font-size:4.4px;line-height:7.6px}
  .three-col.first{left:45px}
  .three-col.third{left:318px}
  .three-col-box{left:168px;top:75px;width:122px;height:143px;background:#f1f1f1}
  .three-col.middle{left:181px;color:var(--dark-text);font-weight:700}

  /* industry */
  .industry-band{left:34px;top:91px;width:408px;height:15px;background:#efefef}
  .industry-col{top:90px;width:80px}
  .industry-num{width:16px;height:16px;border-radius:50%;color:#fff;font-size:5px;font-weight:700;text-align:center;line-height:16px;margin-left:2px}
  .industry-head{font-size:5.6px;font-weight:700;margin-top:3px}
  .industry-list{list-style:none;font-size:4.4px;color:var(--grey-text);line-height:9.6px;margin-top:1px}
  .industry-list li::before{content:"› ";font-weight:700}
  .tone-blue{--tone:var(--brand-blue)}
  .tone-yellow{--tone:var(--yellow)}
  .tone-grey{--tone:#8d8d8d}
  .tone-orange{--tone:var(--orange)}
  .tone-black{--tone:#111}
  .industry-num{background:var(--tone)}
  .industry-head,.industry-list li::before{color:var(--tone)}
  .tone-black .industry-head{color:#111}

  /* heading text */
  .feature-photo{left:0;top:0}
  .feature-title{color:#fff}
  .feature{width:170px}
  .feature-icon{position:absolute;width:17px;height:17px;border-radius:50%;left:-24px;top:0}
  .feature-icon svg{display:block}
  .feature-name{font-size:7.6px;color:#222}
  .feature-desc{font-size:4.7px;line-height:8.4px;color:var(--grey-text);margin-top:3px}

  /* machines */
  .machine-label{width:120px;text-align:center;font-size:9.5px;color:#222}
  .machine-label small{display:block;font-size:4.8px;color:#666;margin-top:1px}
</style>
</head>
<body>

<div class="side-band"></div>
<div class="side-title word-one"><span>P</span><span>O</span><span>W</span><span>E</span><span>R</span><span>P</span><span>O</span><span>I</span><span>N</span><span>T</span></div>
<div class="side-title word-two"><span>D</span><span>E</span><span>S</span><span>I</span><span>G</span><span>N</span></div>

<div class="base-rule"></div>
<div class="base-brand">CRM</div>

<!-- Cover -->
<section class="slide cover col-a row-1">
  <div class="abs cover-photo" role="img" aria-label="Blue size reduction machinery line lit against a dark background"
       style="background:radial-gradient(ellipse at center,#2f5f9e 0%,#1d3c66 45%,#000 75%)"></div>
  <div class="abs cover-title">Corvane Ridge Machinery</div>
  <div class="abs cover-sub">SIZE REDUCTION AND SCREENING</div>
  <div class="abs cover-brand">CRM</div>
</section>

<!-- About Us -->
<section class="slide col-b row-1">
  <svg class="abs about-photo" width="458" height="130" viewBox="0 0 458 130" role="img" aria-label="Greyscale photo of an industrial grinder on site">
    <defs><linearGradient id="aboutGrey" x1="0" y1="0" x2="1" y2="0">
      <stop offset="0" stop-color="#c9c9c9"/><stop offset="0.5" stop-color="#a9a9a9"/><stop offset="1" stop-color="#d2d2d2"/></linearGradient></defs>
    <polygon points="0,0 458,0 458,62 218,118 0,72" fill="url(#aboutGrey)"/>
  </svg>
  <div class="accent"></div>
  <div class="slide-title">About Us</div>
  <div class="abs about-lead">Lorem ipsum dolor<br>sit ametcon<br>sectetur adipiscing</div>
  <div class="abs body-copy about-body">Lorem ipsum dolor sit amet consectetur adipiscing elit. Etiam et convallis orci. Sed sed velit nec mi pellentesque posuere. Donec id fermentum nisl. Nam dictum fringilla nunc, eu porttitor nisi pharetra id. Duis sed finibus augue. Sed quis augue enim. Suspendisse pretium fringilla mi a ferment. Phasellus dolor nibh, eleifend mattis dapibus sed, facilisis non nulla. Vestibulum ante ipsum primis in faucibus orci luctus et ultrices posuere cubilia Curae. Curabitur at nisi ipsum. Mauris at feugiat sapien. Ut finibus bibendum risus vel scelerisque. Aenean quis pretium magna.</div>
  <div class="footer-rule"></div><div class="footer-brand">CRM</div>
</section>

<!-- True Blue -->
<section class="slide col-a row-2">
  <div class="abs heritage-accent"></div>
  <div class="abs heritage-title">True Blue —<br>keeping faith with<br>our heritage of<br>manufacturing skill</div>
  <div class="abs heritage-photo" role="img" aria-label="Blue grinder with yellow safety rails outdoors under a cloudy sky"
       style="background:linear-gradient(180deg,#9aa7b4 0%,#6f86a3 35%,#2f64a8 60%,#3a5d86 80%,#8a7b62 100%)"></div>
  <div class="abs body-copy heritage-body">With over 70 years under our belt, we're not the new kids on the block. We started in regional sawmill operations, where timber grows big and mills grow bigger. We served them. We entered the recycling industry before anyone knew what it was. As our reputation spread, other industries wanted our unique combination of mill-duty machines and systems that delivered reliable operation. We responded to their needs. Corvane Ridge brings customers an over 70 year reputation for performance, durability, and reliability and we're just getting started.</div>
  <div class="footer-rule"></div><div class="footer-brand">CRM</div>
</section>

<!-- Two column -->
<section class="slide col-b row-2">
  <div class="accent"></div>
  <div class="slide-title">Two column text</div>
  <div class="abs body-copy two-col-left">
    <p>Lorem ipsum dolor sit amet, consectetur adipiscing elit. Praesent sodales odio sit amet odio tristique quis tempus odio. Lorem ipsum dolor sit amet, consectetur adipiscing elit. Praesent sodales odio sit amet odio tristique quis tempus odio. Lorem ipsum dolor sit amet, consectetur adipiscing elit. Praesent sodales odio sit amet.</p>
    <p>Lorem ipsum dolor sit amet, consectetur adipiscing elit. Praesent sodales odio sit amet odio tristique quis tempus odio. Lorem ipsum dolor sit amet, consectetur adipiscing elit. Praesent sodales odio sit amet odio tristique quis tempus odio. Lorem ipsum dolor sit amet, consectetur adipiscing elit. Praesent sodales odio sit amet.</p>
  </div>
  <div class="abs two-col-divider"></div>
  <div class="abs body-copy two-col-right">
    <p>Lorem ipsum dolor sit amet, consectetur adipiscing elit. Praesent sodales odio sit amet odio tristique quis tempus odio. Lorem ipsum dolor sit amet, consectetur adipiscing elit. Praesent sodales odio sit amet odio tristique quis tempus odio. Lorem ipsum dolor sit amet, consectetur adipiscing elit. Praesent sodales odio sit amet.</p>
  </div>
  <div class="footer-rule"></div><div class="footer-brand">CRM</div>
</section>

<!-- Three column -->
<section class="slide col-a row-3">
  <div class="accent"></div>
  <div class="slide-title">Three column text</div>
  <div class="abs body-copy three-col first">Lorem ipsum dolor sit amet, consectetur adipiscing elit. Praesent sodales odio sit amet odio tristique quis tempus odio. Lorem ipsum dolor sit amet, consectetur adipiscing elit. Praesent sodales odio sit amet odio tristique quis tempus odio. Lorem ipsum dolor sit amet, consectetur adipiscing elit. Praesent sodales odio sit amet. Lorem ipsum dolor sit amet, consectetur.</div>
  <div class="abs three-col-box"></div>
  <div class="abs body-copy three-col middle">Lorem ipsum dolor sit amet, consectetur adipiscing elit. Praesent sodales odio sit amet odio tristique quis tempus odio. Lorem ipsum dolor sit amet, consectetur adipiscing elit. Praesent sodales odio sit amet odio tristique quis tempus odio. Lorem ipsum dolor sit amet, consectetur adipiscing elit. Praesent sodales odio sit amet. Lorem ipsum dolor sit amet, consectetur.</div>
  <div class="abs body-copy three-col third">Lorem ipsum dolor sit amet, consectetur adipiscing elit. Praesent sodales odio sit amet odio tristique quis tempus odio. Lorem ipsum dolor sit amet, consectetur adipiscing elit. Praesent sodales odio sit amet odio tristique quis tempus odio. Lorem ipsum dolor sit amet, consectetur adipiscing elit. Praesent sodales odio sit amet. Lorem ipsum dolor sit amet, consectetur.</div>
  <div class="footer-rule"></div><div class="footer-brand">CRM</div>
</section>

<!-- Your industry -->
<section class="slide col-b row-3">
  <div class="accent"></div>
  <div class="slide-title">Your industry</div>
  <div class="abs industry-band"></div>
  <div class="abs industry-col tone-blue" style="left:36px">
    <div class="industry-num">01</div>
    <div class="industry-head">Heat/Power</div>
    <ul class="industry-list"><li>Biogas</li><li>Biomass Power</li><li>Energy Crops</li><li>Pellets/Densified Fuels</li></ul>
  </div>
  <div class="abs industry-col tone-yellow" style="left:116px">
    <div class="industry-num">02</div>
    <div class="industry-head">Bio-Fuels/Bio-Refining</div>
    <ul class="industry-list"><li>Ag Residuals</li><li>Biofuel</li><li>Biogas</li><li>Energy Crops</li><li>Ethanol</li></ul>
  </div>
  <div class="abs industry-col tone-grey" style="left:204px">
    <div class="industry-num">03</div>
    <div class="industry-head">Recycling</div>
    <ul class="industry-list"><li>C &amp; D</li><li>Biogas</li><li>Compost</li><li>Green Wood Waste</li><li>Organics Processing</li><li>Pallets</li><li>Urban Wood</li></ul>
  </div>
  <div class="abs industry-col tone-orange" style="left:286px">
    <div class="industry-num">04</div>
    <div class="industry-head">Wood Products</div>
    <ul class="industry-list"><li>Engineered Wood</li><li>Fiberboard/Panels</li><li>Pallets</li><li>Pulp and Paper</li><li>Sawmill</li><li>Veneer</li><li>Woodworking</li></ul>
  </div>
  <div class="abs industry-col tone-black" style="left:375px">
    <div class="industry-num">05</div>
    <div class="industry-head">Mulch/Soils</div>
    <ul class="industry-list"><li>Bark</li><li>Bedding</li><li>Colored Mulch</li><li>Compost</li><li>Organics Processing</li><li>Soils</li></ul>
  </div>
  <div class="footer-rule"></div><div class="footer-brand">CRM</div>
</section>

<!-- Heading text -->
<section class="slide col-a row-4">
  <svg class="abs feature-photo" width="458" height="257" viewBox="0 0 458 257" role="img" aria-label="Greyscale close-up of a screening machine with a perforated drum">
    <defs><linearGradient id="featureGrey" x1="0" y1="0" x2="1" y2="1">
      <stop offset="0" stop-color="#5a5a5a"/><stop offset="0.5" stop-color="#9a9a9a"/><stop offset="1" stop-color="#c8c8c8"/></linearGradient></defs>
    <polygon points="0,0 207,0 320,257 0,257" fill="url(#featureGrey)"/>
  </svg>
  <div class="accent"></div>
  <div class="slide-title feature-title">Heading text</div>
  <div class="abs feature" style="left:258px;top:71px">
    <span class="feature-icon" style="background:var(--brand-blue)"><svg width="17" height="17" viewBox="0 0 17 17"><circle cx="8.5" cy="8.5" r="4" fill="none" stroke="#fff" stroke-width="0.9"/><circle cx="8.5" cy="8.5" r="1.6" fill="none" stroke="#fff" stroke-width="0.9"/></svg></span>
    <div class="feature-name">LOREM IPSUM</div>
    <div class="feature-desc">Lorem ipsum dolor sit amet, consectetuer adipiscing elit, sed diam nonummy nibh euismod tincidunt ut laoreet dolore</div>
  </div>
  <div class="abs feature" style="left:282px;top:123px">
    <span class="feature-icon" style="background:var(--yellow)"><svg width="17" height="17" viewBox="0 0 17 17"><rect x="5" y="5" width="7" height="7" fill="none" stroke="#fff" stroke-width="0.9"/><line x1="6.5" y1="7.5" x2="10.5" y2="7.5" stroke="#fff" stroke-width="0.7"/><line x1="6.5" y1="9.5" x2="10.5" y2="9.5" stroke="#fff" stroke-width="0.7"/></svg></span>
    <div class="feature-name">LOREM IPSUM</div>
    <div class="feature-desc">Lorem ipsum dolor sit amet, consectetuer adipiscing elit, sed diam nonummy nibh euismod tincidunt ut laoreet dolore</div>
  </div>
  <div class="abs feature" style="left:306px;top:175px">
    <span class="feature-icon" style="background:#9a9a9a"><svg width="17" height="17" viewBox="0 0 17 17"><rect x="5" y="7.5" width="7" height="5" fill="none" stroke="#fff" stroke-width="0.9"/><path d="M6.5 7.5 V6 a2 2 0 0 1 4 0 V7.5" fill="none" stroke="#fff" stroke-width="0.9"/></svg></span>
    <div class="feature-name">LOREM IPSUM</div>
    <div class="feature-desc">Lorem ipsum dolor sit amet, consectetuer elit, sed nonummy nibh euismod tincidunt ut laoreet dolore</div>
  </div>
  <div class="footer-rule"></div><div class="footer-brand">CRM</div>
</section>

<!-- Our machines -->
<section class="slide col-b row-4">
  <div class="accent"></div>
  <div class="slide-title">Our machines</div>
  <svg class="abs" style="left:0;top:0" width="458" height="200" viewBox="0 0 458 200">
    <polygon points="126,75 162,75 122,167 62,167" fill="var(--brand-blue)"/>
    <polygon points="218,61 274,61 246,167 174,167" fill="var(--brand-blue)"/>
    <polygon points="350,75 411,75 378,167 302,167" fill="var(--brand-blue)"/>
  </svg>
  <div class="abs" style="left:38px;top:140px;width:80px;height:44px;background:linear-gradient(180deg,#3e78bd,#1f4e8a)" role="img" aria-label="Horizontal grinder machine"></div>
  <div class="abs" style="left:172px;top:124px;width:90px;height:60px;background:linear-gradient(180deg,#4a84c6,#204f8c)" role="img" aria-label="Trommel screen machine"></div>
  <div class="abs" style="left:296px;top:162px;width:120px;height:20px;background:linear-gradient(180deg,#3f78bb,#1f4a82)" role="img" aria-label="Belt conveyor machine"></div>
  <div class="abs machine-label" style="left:36px;top:201px">GRINDERS<small>CRM Size Reduction</small></div>
  <div class="abs machine-label" style="left:170px;top:201px">SCREENS<small>CRM screens</small></div>
  <div class="abs machine-label" style="left:295px;top:201px">CONVEYORS<small>CRM screens &amp; conveyors</small></div>
  <div class="footer-rule"></div><div class="footer-brand">CRM</div>
</section>

</body>
</html>
```